Back Pain

Need a flyer similar to the attached draft. This is to be handed out to prospective patients. Note that Sketch Hive has already designed the logo. If you need a copy please contact me

```html
<!DOCTYPE html>
<html lang="en">
<head>
<meta charset="utf-8">
<title>Spine Ease Clinic – Flyer</title>
<link rel="stylesheet" href="https://fonts.googleapis.com/css2?family=Bebas+Neue&family=Oswald:wght@300;400;500&family=Montserrat:wght@500;600&display=swap">
<style>
  :root {
    --navy: #222f39;
    --green: #8dc63f;
    --blue: #0f6fb8;
    --ink: #232e38;
    --paper: #ffffff;
    --backdrop: #e2e2e2;
    --muted: #a9b0b6;
  }
  * { box-sizing: border-box; margin: 0; padding: 0; }
  html, body { width: 1200px; height: 1200px; overflow: hidden; background: var(--backdrop); }
  .flyer {
    position: absolute; left: 194px; top: 30px;
    width: 1228px; height: 1725px;
    background: var(--paper);
    transform: scale(0.661); transform-origin: top left;
    font-family: "Bebas Neue", "Oswald", sans-serif;
    color: var(--ink);
    overflow: hidden;
  }
  .abs { position: absolute; }

  /* header */
  .header { left: 0; top: 0; width: 1228px; height: 307px; background: var(--navy); }
  .header-band { left: 0; top: 307px; width: 1228px; height: 25px; background: var(--green); }
  .brand-mark { left: 350px; top: 70px; width: 120px; height: 120px; border-radius: 50%; background: var(--green); }
  .brand-name { left: 150px; top: 222px; width: 520px; text-align: center; font-family: "Montserrat", sans-serif; font-weight: 600; font-size: 34px; color: var(--blue); letter-spacing: 0.5px; }
  .brand-tag { left: 150px; top: 262px; width: 520px; text-align: center; font-family: "Montserrat", sans-serif; font-weight: 500; font-size: 17px; color: var(--green); letter-spacing: 4px; }
  .header-divider { left: 714px; top: 85px; width: 1px; height: 195px; background: #3a4752; }
  .partner-note { left: 795px; top: 128px; font-family: "Montserrat", sans-serif; font-weight: 500; font-size: 20px; line-height: 27px; color: var(--muted); }
  .partner-name { left: 795px; top: 192px; font-family: "Oswald", sans-serif; font-weight: 500; font-size: 32px; color: #e8ecef; letter-spacing: 1px; }
  .partner-sub { left: 797px; top: 233px; font-family: "Montserrat", sans-serif; font-weight: 500; font-size: 12px; color: var(--muted); letter-spacing: 2px; }

  /* figure + symptoms */
  .figure { left: 45px; top: 370px; width: 345px; height: 1015px; border-radius: 30px; background: linear-gradient(180deg, #f7cba5 0%, #f7cba5 12%, #335e5c 16%, #335e5c 45%, #002a3a 47%, #002a3a 100%); }
  .symptom { height: 64px; background: var(--green); color: #fff; font-size: 44px; line-height: 68px; padding-left: 22px; border-radius: 0 8px 8px 0; }

  /* chart */
  .chart-title { left: 700px; top: 398px; font-size: 43px; line-height: 52px; color: var(--ink); font-weight: 400; }
  .bar { width: 54px; background: var(--green); color: #fff; text-align: center; font-size: 44px; line-height: 1; padding-top: 6px; }
  .bar-angle { top: 780px; width: 80px; text-align: center; font-size: 48px; color: var(--ink); }
  .axis-line { left: 701px; top: 567px; width: 2px; height: 146px; background: var(--ink); }
  .head-icon { left: 705px; top: 563px; width: 112px; height: 130px; border-radius: 55px 55px 20px 40px; background: var(--navy); }
  .axis-label { left: 967px; top: 621px; width: 300px; transform: rotate(-90deg); transform-origin: center; font-size: 28px; text-align: center; color: var(--ink); }

  /* pie */
  .pie { left: 620px; top: 880px; }
  .stat { left: 820px; }
  .stat-light { font-family: "Oswald", sans-serif; font-weight: 300; font-size: 30px; }
  .stat-bold { font-family: "Oswald", sans-serif; font-weight: 500; font-size: 48px; letter-spacing: -1px; }

  /* message */
  .message { right: 83px; text-align: right; font-family: "Oswald", sans-serif; font-weight: 300; line-height: 1; white-space: nowrap; color: var(--ink); z-index: 2; }
  .message strong { font-weight: 500; color: var(--blue); }

  /* doctor */
  .doctor-card { left: 255px; top: 1437px; width: 493px; height: 223px; background: var(--blue); border-radius: 0 16px 16px 0; }
  .photo-ring { left: 60px; top: 1420px; width: 260px; height: 260px; border-radius: 50%; background: var(--paper); }
  .photo { left: 75px; top: 1435px; width: 230px; height: 230px; border-radius: 50%; background: radial-gradient(circle at 50% 45%, #e9b998 0%, #c89877 30%, #dde9ee 60%, #d8e6ec 100%); }
  .doctor-name { left: 343px; top: 1458px; font-family: "Oswald", sans-serif; font-weight: 500; font-size: 44px; color: #fff; }
  .doctor-rule { left: 343px; top: 1530px; width: 92px; height: 4px; background: var(--green); }
  .doctor-address { left: 343px; top: 1552px; font-family: "Oswald", sans-serif; font-weight: 400; font-size: 27px; color: #fff; }
  .phone-icon { left: 342px; top: 1599px; }
  .phone-number { left: 405px; top: 1594px; font-family: "Oswald", sans-serif; font-weight: 500; font-size: 40px; color: #fff; }

  /* offer */
  .offer { left: 795px; top: 1437px; width: 355px; height: 223px; background: var(--navy); border-radius: 16px; overflow: hidden; }
  .offer-top { left: 0; top: 0; width: 355px; height: 116px; background: var(--green); }
  .offer-big { left: 25px; top: 14px; font-family: "Oswald", sans-serif; font-weight: 500; font-size: 80px; line-height: 90px; color: #fff; }
  .offer-pct { left: 106px; top: 26px; font-family: "Oswald", sans-serif; font-weight: 400; font-size: 30px; line-height: 34px; color: #fff; }
  .offer-what { left: 152px; top: 24px; font-family: "Oswald", sans-serif; font-weight: 500; font-size: 36px; line-height: 42px; color: #fff; }
  .offer-note { left: 0; top: 128px; width: 355px; text-align: center; font-family: "Oswald", sans-serif; font-weight: 300; font-size: 32px; color: #fff; }
  .offer-web { left: 0; top: 176px; width: 355px; text-align: center; font-family: "Oswald", sans-serif; font-weight: 500; font-size: 22px; color: #fff; }
</style>
</head>
<body>
<main class="flyer">
  <header>
    <div class="abs header"></div>
    <div class="abs header-band"></div>
    <div class="abs brand-mark"></div>
    <div class="abs brand-name">SPINE EASE CLINIC</div>
    <div class="abs brand-tag">DR SAM PORTER - CHIROPRACTOR</div>
    <div class="abs header-divider"></div>
    <p class="abs partner-note">Trained at and associated<br>with harlow bros</p>
    <div class="abs partner-name">HARLOW BROS</div>
    <div class="abs partner-sub">CHIROPRACTIC CARE</div>
  </header>

  <section class="symptoms">
    <div class="abs figure" role="img" aria-label="Illustration of a man walking while looking down at his phone"></div>
    <div class="abs symptom" style="left:370px;top:410px;width:205px;">HEADACHES</div>
    <div class="abs symptom" style="left:345px;top:486px;width:175px;">NECK PAIN</div>
    <div class="abs symptom" style="left:300px;top:562px;width:243px;">SHOULDER PAIN</div>
    <div class="abs symptom" style="left:300px;top:638px;width:174px;">BACK PAIN</div>
    <div class="abs symptom" style="left:295px;top:784px;width:313px;">ARM AND HANDPAIN</div>
    <div class="abs symptom" style="left:310px;top:864px;width:168px;">SCIATICA</div>
  </section>

  <section class="chart">
    <h2 class="abs chart-title">AS THE HEAD TILTS FORWARD.<br>MORE FORCE IS PLACED<br>ON THE SPINE</h2>
    <div class="abs axis-line"></div>
    <div class="abs head-icon" role="img" aria-label="Silhouette of a head tilted forward"></div>
    <div class="abs bar" style="left:702px;top:726px;height:44px;">12</div>
    <div class="abs bar" style="left:785px;top:645px;height:125px;padding-top:42px;">27</div>
    <div class="abs bar" style="left:864px;top:578px;height:192px;padding-top:78px;">40</div>
    <div class="abs bar" style="left:945px;top:536px;height:234px;padding-top:84px;">49</div>
    <div class="abs bar" style="left:1026px;top:483px;height:287px;padding-top:110px;">60</div>
    <div class="abs bar-angle" style="left:688px;">0°</div>
    <div class="abs bar-angle" style="left:772px;">15°</div>
    <div class="abs bar-angle" style="left:852px;">30°</div>
    <div class="abs bar-angle" style="left:933px;">45°</div>
    <div class="abs bar-angle" style="left:1014px;">60°</div>
    <div class="abs axis-label">PRESSURE ON THE SPINE (LBS)</div>
  </section>

  <section class="usage">
    <svg class="abs pie" width="180" height="180" viewBox="0 0 180 180" aria-hidden="true">
      <circle cx="90" cy="90" r="88" fill="var(--navy)"/>
      <path d="M90 90 L90 2 A88 88 0 0 1 136.6 164.6 Z" fill="var(--green)"/>
    </svg>
    <div class="abs stat stat-light" style="top:902px;">THE AVERAGE PERSONS SPENDS</div>
    <div class="abs stat stat-bold" style="top:938px;">8-11 HOURS PER DAY</div>
    <div class="abs stat stat-light" style="top:1000px;font-size:34px;">USING ELECTRONIC DEVICES</div>
  </section>

  <section class="message-block">
    <p class="abs message" style="top:1097px;font-size:63px;"><strong>CHIROPRACTIC CARE</strong> CAN HELP</p>
    <p class="abs message" style="top:1177px;font-size:48px;">CORRECT AND PREVENT THESE PROBLEMS</p>
    <p class="abs message" style="top:1242px;font-size:52px;">BY <strong>RESTRORING</strong> AND <strong>MAINTAINING</strong></p>
    <p class="abs message" style="top:1307px;font-size:52px;"><strong>PROPER ALIGNMENT</strong> OF THE <strong>NECK</strong></p>
  </section>

  <footer>
    <div class="abs doctor-card"></div>
    <div class="abs photo-ring"></div>
    <div class="abs photo" role="img" aria-label="Portrait photo of the chiropractor"></div>
    <div class="abs doctor-name">Dr Sam Porter</div>
    <div class="abs doctor-rule"></div>
    <div class="abs doctor-address">Now in Riverton at 42 Mill Street</div>
    <svg class="abs phone-icon" width="48" height="48" viewBox="0 0 48 48" aria-hidden="true">
      <circle cx="24" cy="24" r="24" fill="var(--green)"/>
      <path d="M17 13c1-1 2.5-1 3.3 0l2.6 3.4c.7.9.6 2.1-.2 2.9l-1.8 1.7c1.3 2.8 3.6 5.1 6.4 6.4l1.7-1.8c.8-.8 2-.9 2.9-.2l3.4 2.6c1 .8 1 2.3 0 3.3l-1.6 1.6c-1.3 1.3-3.3 1.7-5 1-6.4-2.6-11.300-7.5-13.9-13.9-.7-1.700-.3-3.700 1-5z" fill="#fff"/>
    </svg>
    <div class="abs phone-number">0400 123 456</div>

    <div class="abs offer">
      <div class="abs offer-top"></div>
      <div class="abs offer-big">50</div>
      <div class="abs offer-pct">%<br>Off</div>
      <div class="abs offer-what">Initial<br>Consultation</div>
      <div class="abs offer-note">If you book online at</div>
      <div class="abs offer-web">www.SpineEaseClinic.com.au</div>
    </div>
  </footer>
</main>
</body>
</html>
```